Photography Studio Prep Guide Design Needed

I have a prep guide I send to all parents who book a session - It is outdated and ugly. I want a gorgeous, clean, modern upscale look for the brochure I send.

I already have the text and can provide photos for the final design. I want the cover to be clean and upscale and modern, with a happy feel.

Target Market(s)

My clients for an upscale Newborn Photography Studio

Requirements
Must have
• space for my photos, an upscale clean feel
Nice to have
• I love color, but don't want the brochure to look busy. I love cream, white, pale pink.

```html
<!DOCTYPE html>
<html lang="en">
<head>
<meta charset="utf-8">
<title>Newborn Session Prep Guide</title>
<link rel="stylesheet" href="https://fonts.googleapis.com/css2?family=Oswald:wght@300;400&family=Open+Sans:wght@400;700&family=Sacramento&family=Italianno&display=swap">
<style>
:root{
  --backdrop:#2b2a2a;
  --paper:#ffffff;
  --pink:#e9a7ae;
  --pink-soft:#f3c9ce;
  --pink-deep:#d9848f;
  --plum:#8a3c63;
  --ink:#3a3a3a;
  --ink-soft:#5a5a5a;
  --violet:#9c7bc2;
}
*{box-sizing:border-box;margin:0;padding:0}
html,body{width:1200px;height:1200px;overflow:hidden;background:var(--backdrop)}
body{position:relative;font-family:"Open Sans",Arial,sans-serif;color:var(--ink)}
.page{position:absolute;background:var(--paper);overflow:hidden;display:flex;flex-direction:column}
.page::after{content:"";position:absolute;inset:10px;border:1px solid var(--pink);pointer-events:none;z-index:3}
.cover{left:54px;top:46px;width:338px;height:491px}
.page-two{left:435px;top:46px;width:338px;height:491px}
.page-three{left:796px;top:46px;width:338px;height:492px}
.page-four{left:222px;top:640px;width:350px;height:494px}
.page-five{left:606px;top:640px;width:346px;height:490px}

.photo{position:relative;flex:none}
.ornament{width:64px;height:18px;margin:8px auto 4px;background:var(--pink-soft);border-radius:9px;flex:none}
.pill{display:block;width:max-content;min-width:84px;margin:5px auto 4px;padding:1px 14px;background:var(--pink);color:#fff;
  font-size:8px;border-radius:7px;text-align:center;position:relative;z-index:4}
.pill.on-band{background:#fff;color:var(--pink-deep);border:1px solid var(--pink-soft)}
.body{font-size:5.6px;line-height:1.42;padding:0 22px;text-align:justify;color:var(--ink-soft)}
.body b{color:var(--ink)}
.band{background:var(--pink);flex:1;position:relative;padding-top:4px}
.band .body{color:#fff}
.band .pill{margin-top:-11px}

/* cover */
.cover-top{height:62px;background:#fff;flex:none}
.cover-top::before,.cover-top::after{content:"";position:absolute;top:0;height:3px;background:var(--pink);width:95px}
.cover-top::before{left:0}.cover-top::after{right:0}
.cover-photo{flex:1;background:radial-gradient(ellipse at 50% 55%,#b9a3dc 0%,#7b4fa6 45%,#4a2b6a 75%,#8c6bb8 100%)}
.brand-box{position:absolute;left:97px;top:8px;width:137px;height:142px;background:rgba(255,255,255,.92);
  border:1px solid var(--pink);z-index:4;display:flex;flex-direction:column;align-items:center;padding-top:18px}
.brand-mark{width:50px;height:50px;border-radius:50%;border:1px solid var(--plum);flex:none}
.brand-name{font-family:"Open Sans",Arial,sans-serif;font-size:7px;color:var(--plum);margin-top:6px;letter-spacing:.5px}
.cover-title{font-family:"Oswald",Arial,sans-serif;font-weight:300;font-size:18px;color:var(--plum);margin-top:8px;letter-spacing:.3px}
.cover-sub{font-family:"Italianno",cursive;font-size:22px;color:var(--plum);line-height:.9}

/* page two */
.script-title{font-family:"Sacramento",cursive;font-size:30px;text-align:center;color:var(--ink);line-height:1.1}
.intro{font-size:7.6px;text-align:center;line-height:1.45;margin:6px 0 4px;color:var(--ink)}
.photo-baby-sleep{height:157px;background:linear-gradient(180deg,#f2efe9,#e9e2d8 60%,#ddd3c6)}
.photo-baby-wrap{height:170px;background:linear-gradient(180deg,#fff 0%,#f1ebe4 30%,#d9cfc4 70%,#3a3f4d 100%);margin-top:6px}

/* page four */
.duo{display:flex;gap:4px;height:208px;flex:none;margin-top:8px}
.photo-pilot{flex:1;background:linear-gradient(180deg,#8fd3cc,#f5f5f2 55%,#e2b34a)}
.photo-fox{flex:1;background:linear-gradient(180deg,#e7e0d6,#d88a4d 45%,#f3ede2)}
.band-bottom .pill{margin-top:-10px}

/* page five */
.photo-crate{height:130px;margin-top:2px;background:linear-gradient(90deg,#6a5038,#b79a72 30%,#1d2536 45%,#1d2536 60%,#b39470 75%,#5d4630)}
.list{list-style:none;padding:4px 20px 0 28px}
.list li{display:flex;gap:8px;font-size:5.8px;line-height:1.4;margin-bottom:10px;color:var(--ink-soft)}
.num{flex:none;width:14px;height:14px;border-radius:50%;background:var(--pink);color:#fff;font-size:8px;
  display:flex;align-items:center;justify-content:center}
.faq{padding:0 22px}
.faq h3{font-weight:400;font-size:10px;color:#fff;display:flex;align-items:center;gap:5px;margin-top:4px}
.faq h3 span{width:9px;height:9px;border-radius:50%;background:#fff;color:var(--pink);font-size:6px;display:flex;align-items:center;justify-content:center}
.faq p{font-size:5.6px;color:#fff;line-height:1.4}
</style>
</head>
<body>

<section class="page cover">
  <div class="cover-top"></div>
  <div class="photo cover-photo" role="img" aria-label="Sleeping newborn in a lavender bonnet wrapped in lilac, nestled among purple roses"></div>
  <div class="brand-box">
    <div class="brand-mark"></div>
    <div class="brand-name">Willow Fern Studio</div>
    <div class="cover-title">NEWBORN SESSION</div>
    <div class="cover-sub">Prep Guide</div>
  </div>
</section>

<section class="page page-two">
  <div class="ornament" role="img" aria-label="Pink bird and flourish ornament"></div>
  <h1 class="script-title">Parent Instructions &amp; Preparations</h1>
  <p class="intro">Congratulations on expecting a baby!<br>Here are my instructions to ensure a successful newborn photography session.<br>Please follow these instructions as closely as possible.</p>
  <span class="pill">1.Nursing</span>
  <p class="body">If you are nursing, please avoid eating anything spicy (hot sauce, hot peppers, curry, etc.) that might upset baby's tummy for 24 hours preceding your scheduled session. Please if you are breastfeeding do NOT drink caffeine or coffee before your session – I know this is hard but baby will be wired if you have caffeine. If you notice baby has a lot of gas after feedings please check with your pediatrician and bring gas drops (Tummy Calm or other brand) to your session. The most common reason a baby will not settle for a session is gas pressure/discomfort.</p>
  <div class="photo photo-baby-sleep" role="img" aria-label="Newborn asleep on a cream blanket beside a small knitted bunny" style="margin-top:8px"></div>
  <div class="band">
    <span class="pill on-band">2.Feeding</span>
    <p class="body">Feed the baby as much as possible in the 24 hours preceding your session – this will help minimize the amount baby needs to feed during the session, and will help baby sleep as long and as soundly as possible. Feed baby 2-3 hours before your session and not again until you arrive. This feeding is planned in your session time and it's not rushed.<br>Please bring an extra bottle of formula or breastmilk to the session if possible – sometimes a small amount of milk in a bottle can quickly soothe a baby back to sleep without requiring a full feeding. I will respect your wishes if you choose not to use a bottle, but please understand we may have to pass on some poses if baby will not settle in position, and I cannot use a bottle to soothe them into the pose.</p>
  </div>
</section>

<section class="page page-three">
  <div class="ornament" role="img" aria-label="Pink bird and flourish ornament"></div>
  <span class="pill">3. Keep Baby A Wake</span>
  <p class="body">Interact with, and <b>keep baby awake for 2 hours preceding your appointment to make sure they are nice and sleepy for their session.</b> A great way to do this is by giving baby a bath – which will get them nice and clean and keep them awake. Also – keeping baby naked, in a diaper only is a good way to keep them awake and alert. This step is extremely important – <b>otherwise it can take a long time to get baby to sleep, and we will have less time for photos.</b></p>
  <span class="pill">4. Clothes</span>
  <p class="body">Please dress baby in a simple loose sleeper we can just unsnap when you arrive – we want to keep baby as calm and happy as possible and want to avoid clothes we have to pull over their head. I provide all clothing/hats/props at your session.</p>
  <span class="pill">5. Pacifier</span>
  <p class="body">Please bring a pacifier – it can be very helpful during a session if a baby is fussy. Please note I only use the pacifier for a few minutes at a time to soothe into a pose. <b>If you choose not to bring a pacifier I will respect your decision, but please understand we may have to pass on several poses if you do not bring one.</b></p>
  <span class="pill">6. Studio</span>
  <p class="body">My studio is kept VERY warm to make sure your baby is comfortable through the whole session. It will be around 75-80 degrees so please dress in layers for comfort. I will have cold bottles of water available during your session. <b>Please note – if you ask me to turn the heat down, or tell me it is too warm for baby, I cannot guarantee any results for your session.</b> Babies are used to 98.6 degrees in the womb, and a cold studio will wake baby immediately. Babies do not wear much during their sessions and lose heat quickly. If you ask me to turn the heat down, and baby is fussy I will finish the session with only swaddled poses, or with parents. It is not safe to put an awake, alert baby in any props.</p>
  <div class="photo photo-baby-wrap" role="img" aria-label="Newborn resting chin on hands in a navy wrap on a cream blanket"></div>
  <div class="band">
    <span class="pill on-band">7.Keep Baby A Wake</span>
    <p class="body">Your role at this session is to sit back and relax. I need very little assistance during the session, and want you to take this time to rest, relax and enjoy the session. Feel free to nap, catch up on work, thank you notes, or whatever you like. If baby needs to feed during the session that will be your only task! I will occasionally ask for a spotter for safety on some poses.</p>
  </div>
</section>

<section class="page page-four">
  <div class="ornament" role="img" aria-label="Pink bird and flourish ornament"></div>
  <span class="pill">8. Time</span>
  <p class="body">Your session will last between 2-4 hours – please keep this in mind. I will provide bottled water and light snacks (granola bars/pretzels/etc.) but you may want to bring more food since the session can last up to 4 hours. Please note that I cannot shoot past 4 hours – if baby is fussy I will do my best to get beautiful photos. At 3 hours if baby is still fussy I will let you know that we need to switch to swaddled/wrapped poses to finish the session. Or we can do more family photos as well.</p>
  <span class="pill">9. Family photos/clothing</span>
  <p class="body">I highly recommend mom and dad wear simple white/cream shirts, or black/navy shirts which will keep the focus on the baby. Mom can choose a tank top or dress as well. That is only a suggestion, and of course you are welcome to wear anything you choose. If dad is comfortable baring his chest it can make for some beautiful images, but that is totally up to the comfort of dad! My photos of newborns with mom/dad are generally from the waist up, so your pants or shoes will not matter.</p>
  <div class="duo">
    <div class="photo photo-pilot" role="img" aria-label="Newborn in a sailor cap asleep on a toy airplane among clouds"></div>
    <div class="photo photo-fox" role="img" aria-label="Newborn in a knitted fox hat swaddled in cream with a plush fox"></div>
  </div>
  <div class="band band-bottom">
    <span class="pill on-band">10. Sibling Photos</span>
    <p class="body">Photos of your newborn with their sibling(s) are included, and will be done at the very beginning of the session. I recommend having sibling boys wear cream/white tops or plain dark shirts with jeans. Sibling girls can wear cream/white shirts/tank tops with jeans or cream/white dresses.</p>
    <p class="body" style="margin-top:6px"><b style="color:#fff">I do not recommend bringing toddlers/children for the entire session. It is very hot in my studio and there is not adequate room for them to play, which makes them unhappy! Please plan to bring them for photos at the beginning of the session, and have dad or a grandparent take them out for an activity while we finish the session.</b></p>
  </div>
</section>

<section class="page page-five">
  <div class="ornament" role="img" aria-label="Pink bird and flourish ornament"></div>
  <div class="photo photo-crate" role="img" aria-label="Newborn in a mint knitted hat tucked into a rustic wooden crate"></div>
  <h2 class="script-title" style="font-size:22px;margin-top:4px">What I need to know before your session</h2>
  <ol class="list">
    <li><span class="num">1</span><span>Please e-mail me with the baby's birth date, birth weight, sex, and name. Remember, my newborn sessions take place between 5-11 days old, so it is critical to e-mail me when baby arrives to schedule your session.</span></li>
    <li><span class="num">2</span><span>If you have any favorite colors please feel free to let me know and I will be happy to work them into your session. Please also let me know if there are any colors you do not want used during your session. You can create an account on my website and select a set of favorites, I will look at those before your session.</span></li>
    <li><span class="num">3</span><span>If you have specific shots in mind for your session, or any props you have seen on my website that you would like me to use, you must let me know in advance. It takes a lot of preparation for a session, so please tell me beforehand if you have a specific request.</span></li>
    <li><span class="num">4</span><span>Please let me know if you have any siblings you would like to include in the session and their age(s).</span></li>
  </ol>
  <div class="band">
    <span class="pill on-band">Faq's</span>
    <div class="faq">
      <h3><span>1</span>When Will I See My Photos?</h3>
      <p>Your gallery of images will be e-mailed to you within 3 weeks. You will receive a preview photo of your session within 2 days.</p>
      <h3><span>2</span>Can I Share My Gallery?</h3>
      <p>Your gallery of images will be e-mailed to you within 3 weeks. You will receive a preview photo of your session within 2 days.</p>
      <h3><span>3</span>When Will I See My Photos?</h3>
      <p>You Can Download All Of Your High-resolution Images Directly From Your Gallery.<br>Please Keep In Mind That These Are Very Large Files – Each Photo Can Be Up To 10 Megabytes.</p>
    </div>
  </div>
</section>

</body>
</html>
```